Pool Services Flyer promote regular pool services

We need a flyer design to be send out as a DL Postcard

We are a pool and spa maintenance business and would like to promote of regular pool services.
Please see our website www.brightripplepoolcare.com.au and our facebook page https://www.facebook.com/pages/Bright-Ripple-Pool-Care/583920174630518

We are pretty flexible with layouts etc Our monthly pool service is $67.00 plus chemicals so we would like this highlighted on our ad. We also so one off, weekly and fortnightly services as well.

We would like our details and logo on front and website also listed.

Target Market(s)

Pool owners

Industry/Entity Type

Pool Service

Colors
33a6d7
0292cd
0555a3
3276b5
85abd2

Requirements
Must have
• Logo
• website address
• phone number
• Price
• Promote the fact that customer wont have to worry about their pool
Nice to have
• like to have a blue wave down the bottom of flyer witht eh contact information in it. Would like to to be crisp not over crowed with information

```html
<!DOCTYPE html>
<html lang="en">
<head>
<meta charset="UTF-8">
<title>Bright Ripple Pool Care – Monthly Pool Service</title>
<link rel="stylesheet" href="https://fonts.googleapis.com/css2?family=Open+Sans:wght@400;600;700;800&display=swap">
<style>
  :root {
    --sky-light: #e8f5fc;
    --sky: #bfe4f6;
    --aqua: #33a6d7;
    --blue: #0292cd;
    --navy: #0555a3;
    --mid-blue: #3276b5;
    --soft-blue: #85abd2;
    --orange: #f26522;
    --text-dark: #1d1d1b;
    --white: #ffffff;
  }
  * { margin: 0; padding: 0; box-sizing: border-box; }
  html, body { width: 1200px; height: 743px; overflow: hidden; background: #fff; }
  body { font-family: "Open Sans", Arial, sans-serif; }

  .postcard {
    position: relative;
    width: 1200px;
    height: 743px;
    overflow: hidden;
    background: linear-gradient(100deg, var(--white) 0%, var(--sky-light) 30%, var(--sky) 75%, #a9daf2 100%);
  }

  .swimmer-art {
    position: absolute;
    z-index: 0;
    left: 420px;
    top: 30px;
    width: 760px;
    height: 480px;
    border-radius: 48% 52% 45% 55% / 55% 45% 55% 45%;
    background: radial-gradient(ellipse at 55% 45%, #3aa0dc 0%, #7cc4ea 40%, rgba(191,228,246,0.4) 72%, rgba(191,228,246,0) 100%);
  }

  .brand {
    position: absolute;
    z-index: 2;
    left: 60px;
    top: 90px;
    width: 340px;
    display: flex;
    flex-direction: column;
    align-items: center;
    gap: 22px;
  }
  .brand-dot {
    width: 120px;
    height: 120px;
    border-radius: 50%;
    background: var(--aqua);
    flex: none;
  }
  .brand-name {
    font-weight: 600;
    font-size: 38px;
    line-height: 1.15;
    text-align: center;
    color: var(--text-dark);
  }

  .website {
    position: absolute;
    z-index: 2;
    left: 46px;
    top: 374px;
    font-size: 19px;
    font-weight: 600;
    color: var(--navy);
  }

  .waves { position: absolute; z-index: 1; left: 0; top: 0; }

  .contact {
    position: absolute;
    z-index: 2;
    left: 30px;
    top: 636px;
  }
  .contact-phone {
    display: flex;
    align-items: center;
    gap: 14px;
    font-size: 44px;
    font-weight: 700;
    line-height: 1.1;
    color: var(--orange);
    letter-spacing: 0.5px;
  }
  .contact-social {
    display: flex;
    align-items: center;
    gap: 10px;
    margin-top: 10px;
    font-size: 19px;
    font-weight: 600;
    color: var(--navy);
  }
  .icon-circle {
    width: 26px;
    height: 26px;
    border-radius: 50%;
    background: var(--orange);
    flex: none;
  }

  .price-badge { position: absolute; z-index: 3; left: 850px; top: 440px; }
  .badge-label {
    font-family: "Open Sans", Arial, sans-serif;
    font-weight: 800;
    fill: var(--navy);
  }
  .badge-price {
    font-family: "Open Sans", Arial, sans-serif;
    font-weight: 800;
    fill: var(--white);
  }
</style>
</head>
<body>
<main class="postcard">

  <div class="swimmer-art" role="img" aria-label="Illustration of a woman swimming underwater through a blue water splash"></div>

  <div class="brand">
    <span class="brand-dot"></span>
    <span class="brand-name">Bright Ripple<br>Pool Care</span>
  </div>

  <p class="website">www.brightripplepoolcare.com.au</p>

  <svg class="waves" width="1200" height="743" viewBox="0 0 1200 743" aria-hidden="true">
    <defs>
      <linearGradient id="wave-aqua" x1="0" y1="0" x2="1" y2="0">
        <stop offset="0" stop-color="#8fd3ef"/>
        <stop offset="1" stop-color="#33a6d7"/>
      </linearGradient>
      <linearGradient id="wave-deep" x1="0" y1="0" x2="1" y2="0">
        <stop offset="0" stop-color="#3276b5"/>
        <stop offset="1" stop-color="#0555a3"/>
      </linearGradient>
    </defs>
    <path d="M0 560 C 250 470, 520 520, 760 500 S 1100 470, 1200 430 L1200 743 L0 743 Z" fill="url(#wave-aqua)" opacity="0.55"/>
    <path d="M0 600 C 260 520, 560 560, 800 555 S 1080 540, 1200 500 L1200 743 L0 743 Z" fill="url(#wave-deep)"/>
    <path d="M0 625 C 280 560, 580 590, 820 585 S 1090 570, 1200 540 L1200 743 L0 743 Z" fill="var(--blue)"/>
    <path d="M0 642 C 300 590, 600 615, 850 610 S 1100 600, 1200 580 L1200 743 L0 743 Z" fill="var(--white)"/>
    <path d="M0 740 C 300 720, 700 735, 1200 700 L1200 743 L0 743 Z" fill="var(--sky)" opacity="0.6"/>
  </svg>

  <div class="contact">
    <p class="contact-phone">
      <svg width="34" height="34" viewBox="0 0 34 34" aria-hidden="true">
        <circle cx="17" cy="17" r="17" fill="var(--orange)"/>
        <path d="M12 9 l4 4 -2 2.5 c1 2 2.5 3.5 4.5 4.5 l2.5-2 4 4 -2.5 3 c-6 -0.5 -12 -6.5 -12.5 -12.5 Z" fill="#fff"/>
      </svg>
      (02) 4821 3057
    </p>
    <p class="contact-social">
      <span class="icon-circle"></span>
      www.facebook.com/pages/Bright-Ripple-Pool-Care/
    </p>
  </div>

  <svg class="price-badge" width="280" height="280" viewBox="0 0 300 300" role="img" aria-label="Our monthly pool service $67.00 plus chemicals">
    <circle cx="150" cy="150" r="146" fill="var(--navy)"/>
    <circle cx="150" cy="150" r="132" fill="var(--white)"/>
    <circle cx="150" cy="150" r="122" fill="var(--mid-blue)"/>
    <circle cx="150" cy="150" r="100" fill="var(--white)"/>
    <g fill="var(--white)">
      <circle cx="150" cy="39" r="4"/><circle cx="150" cy="261" r="4"/>
      <circle cx="39" cy="150" r="4"/><circle cx="261" cy="150" r="4"/>
      <circle cx="72" cy="72" r="4"/><circle cx="228" cy="72" r="4"/>
      <circle cx="72" cy="228" r="4"/><circle cx="228" cy="228" r="4"/>
    </g>
    <text class="badge-label" x="150" y="108" font-size="19" text-anchor="middle">OUR MONTHLY</text>
    <text class="badge-label" x="150" y="130" font-size="19" text-anchor="middle">POOL SERVICE</text>
    <path d="M40 145 L64 145 L56 160 L64 175 L40 175 Z" fill="#c44b12"/>
    <path d="M260 145 L236 145 L244 160 L236 175 L260 175 Z" fill="#c44b12"/>
    <rect x="58" y="138" width="184" height="44" fill="var(--orange)"/>
    <text class="badge-price" x="150" y="173" font-size="36" text-anchor="middle">$67.00</text>
    <text class="badge-label" x="150" y="208" font-size="16" text-anchor="middle">PLUS</text>
    <text class="badge-label" x="150" y="227" font-size="16" text-anchor="middle">CHEMICALS</text>
  </svg>

</main>
</body>
</html>
```